IT Company needs a Wordpress Web Design

We need a wordpress website for a new IT Company called 'RJ Systemworks'. We develop educational software for Middle and High School Students and Staff. Our initial product is DeskRoute - a web app that allows School Counselors to track information about the students that they see. We would like to see modern designs that include the company logo and the DeskRoute logo

Target Market(s)

Educators

Industry/Entity Type

Information Technology

Coding

Coded - Design and coding required

Number of Pages Required

1 page

Font styles to use
Sans Serif

Requirements
Must have
• Must be able to use WordPress
Should not have
• No Flash

```html
<!DOCTYPE html>
<html lang="en">
<head>
<meta charset="utf-8">
<title>RJ Systemworks</title>
<link rel="stylesheet" href="https://fonts.googleapis.com/css2?family=Nunito+Sans:wght@400;600;700;800&display=swap">
<style>
:root{
  --blue:#4a86c1;
  --blue-dark:#3f78b0;
  --orange:#f39a12;
  --ink:#333840;
  --muted:#6b7078;
  --soft:#f7f7f7;
  --softer:#fafafa;
  --circle:#f5f5f5;
  --white:#ffffff;
  --brand-red:#c8202f;
}
*{margin:0;padding:0;box-sizing:border-box}
html,body{width:1200px;height:2951px;overflow:hidden}
body{position:relative;background:var(--white);font-family:"Nunito Sans",Arial,sans-serif;color:var(--ink)}
.abs{position:absolute}

/* header */
.site-header{position:absolute;left:0;top:0;width:1200px;height:112px;background:var(--white)}
.brand{position:absolute;left:144px;top:40px;font-size:22px;font-weight:800;color:var(--blue);letter-spacing:.2px}
.main-nav{position:absolute;top:50px;font-size:14px;font-weight:700;color:#111}
.main-nav a{position:absolute;white-space:nowrap;color:inherit;text-decoration:none}
.nav-active{position:absolute;left:586px;top:78px;width:50px;height:3px;background:var(--blue)}

/* hero */
.hero{position:absolute;left:0;top:112px;width:1200px;height:620px;
  background:linear-gradient(100deg,#c9b4a4 0%,#b89a86 18%,#d8dde4 34%,#8ea1b8 52%,#e9eaec 70%,#f3f1ee 100%)}
.hero-dots{position:absolute;left:48px;top:580px}
.hero-dots span{position:absolute;left:0;width:10px;height:10px;border-radius:50%;background:var(--white)}
.hero-dots span.active{background:#7d8590}
.hero-card{position:absolute;left:606px;top:287px;width:413px;height:323px;background:rgba(74,134,193,.93)}
.hero-title{position:absolute;left:27px;top:56px;width:370px;font-size:28px;line-height:36px;font-weight:700;color:var(--white)}
.hero-btn{position:absolute;left:29px;top:228px;width:171px;height:49px;background:var(--white);
  color:#222;font-size:13px;font-weight:700;letter-spacing:.3px;text-align:center;line-height:49px}

/* features */
.feature{position:absolute;top:802px;width:240px;text-align:center}
.feature-circle{width:240px;height:240px;border-radius:50%;background:var(--circle);display:flex;align-items:center;justify-content:center}
.feature-circle.active{background:var(--blue)}
.feature-label{margin-top:32px;font-size:18px;font-weight:600;color:#2d2d2d}

/* product */
.product{position:absolute;left:0;top:1172px;width:1200px;height:382px;background:var(--soft)}
.product-name{position:absolute;left:220px;top:114px;font-size:30px;font-weight:800;color:var(--brand-red)}
.product-text{position:absolute;left:216px;top:190px;width:340px;font-size:18px;line-height:29px;color:#3a3a3a}
.product-photo{position:absolute;left:600px;top:65px;width:425px;height:248px;
  background:linear-gradient(90deg,#b98e72 0%,#e7e0d6 30%,#6fb8d0 55%,#8fd0b4 75%,#d8c6b2 100%)}

/* faq */
.section-title{position:absolute;left:0;width:1200px;text-align:center;font-size:28px;font-weight:600;color:#3a3a3a}
.faq-tabs{position:absolute;top:1688px;font-size:22px;font-weight:600;color:#9aa0a6}
.faq-tabs span{position:absolute;white-space:nowrap}
.faq-tabs .active{color:var(--blue)}
.faq-band{position:absolute;left:0;top:1750px;width:1200px;height:296px;background:var(--softer)}
.faq-item{position:absolute;top:52px;width:300px}
.faq-q{font-size:17px;line-height:26px;font-weight:700;color:#3a3a3a;height:76px}
.faq-a{margin-top:12px;font-size:13px;line-height:21px;color:#666}

/* pricing */
.plan{position:absolute;top:2168px;width:444px;height:369px;background:var(--blue);color:var(--white)}
.plan-title{position:absolute;left:23px;top:60px;font-size:28px;line-height:34px;font-weight:600}
.plan-price{position:absolute;right:0;top:43px;width:177px;height:96px;background:var(--orange);
  font-size:30px;font-weight:700;line-height:96px;text-align:center}
.plan-price small{font-size:11px;font-weight:600}
.plan-list{position:absolute;left:20px;top:153px;list-style:none;font-size:11px}
.plan-list li{height:38px;line-height:16px}
.plan-list li::before{content:"›";display:inline-block;width:26px;font-size:13px}

/* footer */
.site-footer{position:absolute;left:0;top:2616px;width:1200px;height:285px;background:var(--softer)}
.footer-brand{position:absolute;left:144px;top:50px;font-size:22px;font-weight:800;color:var(--blue)}
.footer-col{position:absolute;top:60px}
.footer-col h4{font-size:13px;font-weight:800;color:#111;margin-bottom:33px}
.footer-col a{display:block;font-size:13px;line-height:29px;color:#222;text-decoration:none}
.social{display:flex;gap:14px;margin-top:2px}
.social span{width:10px;height:10px;border-radius:50%;background:var(--blue)}
.copyright{position:absolute;left:0;top:2901px;width:1200px;height:50px;line-height:48px;text-align:center;font-size:11px;font-weight:600;color:#222}
</style>
</head>
<body>

<header class="site-header">
  <div class="brand">RJ Systemworks</div>
  <nav class="main-nav">
    <a style="left:586px">Home</a>
    <a style="left:677px">About Us</a>
    <a style="left:787px">Services</a>
    <a style="left:891px">FAQ's</a>
    <a style="left:980px">Contact Us</a>
  </nav>
  <div class="nav-active"></div>
</header>

<section class="hero" role="img" aria-label="Photo of a smiling student at a desk in a classroom">
  <div class="hero-dots">
    <span class="active" style="top:0"></span>
    <span style="top:22px"></span>
    <span style="top:44px"></span>
    <span style="top:66px"></span>
  </div>
  <div class="hero-card">
    <h1 class="hero-title">We develop educational software for Middle &amp; High School Students and Staff</h1>
    <div class="hero-btn">LEARN MORE</div>
  </div>
</section>

<div class="feature" style="left:167px">
  <div class="feature-circle active" role="img" aria-label="Student illustration icon"></div>
  <div class="feature-label">Info Of Students</div>
</div>
<div class="feature" style="left:478px">
  <div class="feature-circle">
    <svg width="100" height="120" viewBox="0 0 100 120" fill="none" stroke="#4a86c1" stroke-width="3" stroke-linejoin="round">
      <circle cx="50" cy="45" r="32"/>
      <circle cx="50" cy="45" r="22"/>
      <path d="M50 30l5 10 11 1.5-8 7.5 2 11-10-5.5-10 5.5 2-11-8-7.5 11-1.5z"/>
      <path d="M32 72l-10 38 14-8 8 14 8-30"/>
      <path d="M68 72l10 38-14-8-8 14-8-30"/>
    </svg>
  </div>
  <div class="feature-label">Behaviour Student</div>
</div>
<div class="feature" style="left:789px">
  <div class="feature-circle">
    <svg width="110" height="110" viewBox="0 0 110 110" fill="none" stroke="#4a86c1" stroke-width="3" stroke-linejoin="round">
      <path d="M10 45L100 8 80 80 55 62z"/>
      <path d="M100 8L45 58v25l10-21"/>
      <path d="M30 95c10 8 30 8 45 0" stroke-dasharray="6 6"/>
    </svg>
  </div>
  <div class="feature-label">Track Student</div>
</div>

<section class="product">
  <div class="product-name">DeskRoute</div>
  <p class="product-text">A web app that allows School Counselors to track information about the students that they see</p>
  <div class="product-photo" role="img" aria-label="Photo of young students working at classroom desks"></div>
</section>

<h2 class="section-title" style="top:1614px">Frequently Asked Questions</h2>
<div class="faq-tabs">
  <span class="active" style="left:448px">What</span>
  <span style="left:545px">Why</span>
  <span style="left:623px">How</span>
  <span style="left:706px">Who</span>
</div>
<section class="faq-band">
  <div class="faq-item" style="left:144px">
    <div class="faq-q">What is DeskRoute ?</div>
    <p class="faq-a">Sed ut perspiciatis unde omnis iste natus error sit voluptatem accusantium doloremque laudantium, totam rem aperiam, eaque ipsa quae</p>
  </div>
  <div class="faq-item" style="left:458px">
    <div class="faq-q">What I need in order to<br>run DeskRoute ?</div>
    <p class="faq-a">Sed ut perspiciatis unde omnis iste natus error sit voluptatem accusantium doloremque laudantium, totam rem aperiam, eaque ipsa quae</p>
  </div>
  <div class="faq-item" style="left:770px">
    <div class="faq-q">What types of reports can<br>I generate with DeskRoute ?</div>
    <p class="faq-a">Sed ut perspiciatis unde omnis iste natus error sit voluptatem accusantium doloremque laudantium, totam rem aperiam, eaque ipsa quae</p>
  </div>
</section>

<h2 class="section-title" style="top:2090px">Price Plans</h2>
<div class="plan" style="left:144px">
  <div class="plan-title">Individual<br>School Purchase</div>
  <div class="plan-price">$200/<small>School</small></div>
  <ul class="plan-list">
    <li>12months of access to DeskRoute</li>
    <li>Individual accounts for each school counsellor in your office</li>
    <li>Customizable student login screen</li>
    <li>Access to a variety of data reports in excel and PDF format</li>
    <li>E-mail Product Support</li>
  </ul>
</div>
<div class="plan" style="left:614px">
  <div class="plan-title">District Level<br>Purchase</div>
  <div class="plan-price">$150/<small>School</small></div>
  <ul class="plan-list">
    <li>12months of access to DeskRoute</li>
    <li>District level access to information and reports</li>
    <li>District level account controls</li>
    <li>Access to a variety of data reports in excel and PDF format</li>
    <li>E-mail Product Support</li>
  </ul>
</div>

<footer class="site-footer">
  <div class="footer-brand">RJ Systemworks</div>
  <div class="footer-col" style="left:336px">
    <h4>Quick Links</h4>
    <a>Home</a><a>About Us</a><a>Services</a><a>FAQ's</a><a>Contact Us</a>
  </div>
  <div class="footer-col" style="left:586px">
    <h4>Other Links</h4>
    <a>Privacy Policy</a><a>Terms Of Service</a><a>Disclaimer</a>
  </div>
  <div class="footer-col" style="left:818px">
    <h4>Connect With Us</h4>
    <div class="social"><span></span><span></span><span></span><span></span><span></span></div>
  </div>
</footer>
<div class="copyright">© 2017 Company Name &nbsp; | &nbsp; All Rights Reserved</div>

</body>
</html>
```